Letterhead, business card and email signature design

I have a new company and I would like a professional letterhead, business card and email signature designed. Id like the business card to have room for a photo of the bearer. I'd also like the template to be editable so we can adapt for future members of staff etc.

```html
<!DOCTYPE html>
<html lang="en">
<head>
<meta charset="utf-8">
<title>Halvern Systems – Stationery Set</title>
<link href="https://fonts.googleapis.com/css2?family=Lato:wght@400;700&family=Open+Sans:wght@300;400&display=swap" rel="stylesheet">
<style>
:root{
  --navy:#1b3358;
  --navy-deep:#142848;
  --maroon:#8e2444;
  --paper:#e6e6e8;
  --paper-light:#ececee;
  --ink:#3b4250;
  --ink-soft:#7a8090;
  --backdrop:#5a5c60;
}
*{box-sizing:border-box;margin:0;padding:0}
html,body{width:1200px;height:760px;overflow:hidden}
body{background:var(--backdrop);font-family:"Lato",sans-serif;color:var(--ink);position:relative}
.piece{position:absolute;background:var(--paper)}
.icon{width:6px;height:6px;fill:var(--navy);vertical-align:-1px;margin-right:4px}

.wordmark{display:flex;align-items:center;gap:6px;font-family:"Lato",sans-serif;font-weight:700;color:var(--navy);letter-spacing:.04em;white-space:nowrap}
.wordmark .dot{border-radius:50%;background:var(--maroon);flex:none}

/* business card front */
.card-front{left:124px;top:56px;width:217px;height:122px;background:linear-gradient(135deg,var(--navy) 0%,var(--navy-deep) 100%)}
.card-front .wordmark{position:absolute;left:52px;top:50px;font-size:13px;color:#fff}
.card-front .wordmark .dot{width:14px;height:14px;background:#fff}
.card-front .web{position:absolute;left:0;right:0;bottom:15px;text-align:center;font-size:5px;color:#d7dbe4}

/* business card back */
.card-back{left:369px;top:56px;width:216px;height:122px}
.portrait{border-radius:50%;background:radial-gradient(circle at 50% 40%,#c9a08a 0%,#7b8aa3 55%,#4f6a96 100%);border:2px solid var(--navy)}
.card-back .portrait{position:absolute;left:41px;top:38px;width:46px;height:46px}
.card-back .details{position:absolute;left:122px;top:33px;font-size:4.6px;line-height:6.2px;color:var(--ink)}
.card-back .name{font-size:6.6px;font-weight:700;color:var(--navy);line-height:7px}
.card-back .role{margin-bottom:8px}
.card-back .address{margin-bottom:4px}
.card-back .icon{width:4px;height:4px;margin-right:2px}

/* envelope front */
.envelope-front{left:38px;top:209px;width:545px;height:236px}
.envelope-front .wordmark{position:absolute;left:34px;top:36px;font-size:16px}
.envelope-front .wordmark .dot{width:22px;height:22px}
.envelope-front .contact{position:absolute;left:34px;top:161px;font-size:7.6px;line-height:9px;color:var(--ink)}
.envelope-front .contact .address{margin-top:3px}

/* envelope back */
.envelope-back{left:38px;top:477px;width:545px;height:236px;background:var(--paper-light)}
.envelope-back .flap{position:absolute;left:0;top:0;width:545px;height:77px}
.envelope-back .wordmark{position:absolute;left:0;right:0;top:25px;justify-content:center;font-size:14px;color:#fff}
.envelope-back .wordmark .dot{width:18px;height:18px;background:#fff}
.envelope-back .return{position:absolute;left:122px;top:190px;width:300px;text-align:center;font-size:7.8px;line-height:9px;color:var(--ink);white-space:nowrap}
.envelope-back .return strong{display:block}

/* letterhead */
.letterhead{left:629px;top:39px;width:523px;height:673px;background:linear-gradient(180deg,#e4e4e6 0%,#dedee0 60%,#e2e2e4 100%)}
.letterhead .wordmark{position:absolute;left:26px;top:29px;font-size:16px}
.letterhead .wordmark .dot{width:24px;height:24px}
.letterhead .masthead-contact{position:absolute;left:359px;top:21px;padding-left:12px;border-left:1px solid #55606f;font-size:8px;line-height:9.6px;color:var(--ink)}
.letterhead .letter{position:absolute;left:53px;top:125px;width:420px;font-family:"Open Sans",sans-serif;font-weight:300;font-size:8.6px;line-height:13px;color:var(--ink-soft);text-align:justify}
.letterhead .letter p{margin-bottom:13px}
.letterhead .letter .greeting{text-align:left;margin-bottom:13px}
.letterhead .letter .closing{margin-top:32px}

/* email signature */
.signature{left:449px;top:595px;width:404px;height:89px;background:#e4e4e6;border:1px solid #c9cacd;z-index:2}
.signature .portrait{position:absolute;left:48px;top:19px;width:50px;height:50px}
.signature .person{position:absolute;left:140px;top:17px;font-size:7px;line-height:9px;color:var(--ink)}
.signature .person .name{font-size:8.6px;font-weight:700;color:var(--navy)}
.signature .person .role{margin-bottom:10px}
.signature .office{position:absolute;left:247px;top:56px;font-size:7px;line-height:9px}
.signature .office strong{color:var(--navy)}
.signature .wordmark{position:absolute;left:312px;top:18px;font-size:9px}
.signature .wordmark .dot{width:14px;height:14px}
</style>
</head>
<body>
<svg width="0" height="0" style="position:absolute" aria-hidden="true">
  <defs>
    <symbol id="i-phone" viewBox="0 0 10 10"><path d="M2 0.5l2 2-1 1.2c.6 1.3 1.6 2.3 2.9 2.9L7.1 5.6l2 2-1.2 1.6C4.2 9 1 5.8.8 2.1z"/></symbol>
    <symbol id="i-mail" viewBox="0 0 10 10"><path d="M0 2h10v6H0z M1 3v.2l4 2.6 4-2.6V3z M1 4.4V7h8V4.4L5 7z" fill-rule="evenodd"/></symbol>
    <symbol id="i-web" viewBox="0 0 10 10"><circle cx="5" cy="5" r="4.5"/><path d="M.8 5h8.4M5 .5v9" stroke="#fff" stroke-width=".8"/></symbol>
  </defs>
</svg>

<section class="piece card-front" aria-label="Business card front">
  <div class="wordmark"><span class="dot"></span>HALVERN SYSTEMS</div>
  <p class="web">www.<strong>halvernsystems</strong>.com.au</p>
</section>

<section class="piece card-back" aria-label="Business card back">
  <div class="portrait" role="img" aria-label="Portrait photo of the card holder"></div>
  <div class="details">
    <p class="name">Daniel Mercer</p>
    <p class="role">Chief Executive Officer</p>
    <p class="address">Bellmont House<br>Level 3, 14 Kestrel Lane<br>Northbridge, WA 6003</p>
    <p><svg class="icon"><use href="#i-phone"/></svg>+61 8 5550 1234</p>
    <p><svg class="icon"><use href="#i-mail"/></svg>hello@halvernsystems.com.au</p>
    <p><svg class="icon"><use href="#i-web"/></svg>www.halvernsystems.com.au</p>
  </div>
</section>

<section class="piece envelope-front" aria-label="Envelope front">
  <div class="wordmark"><span class="dot"></span>HALVERN SYSTEMS</div>
  <div class="contact">
    <p><svg class="icon"><use href="#i-phone"/></svg>+61 8 5550 1234</p>
    <p><svg class="icon"><use href="#i-mail"/></svg>hello@halvernsystems.com.au</p>
    <p><svg class="icon"><use href="#i-web"/></svg>www.halvernsystems.com.au</p>
    <p class="address">Bellmont House<br>Level 3, 14 Kestrel Lane, Northbridge, WA 6003</p>
  </div>
</section>

<section class="piece envelope-back" aria-label="Envelope back">
  <svg class="flap" viewBox="0 0 545 77" aria-hidden="true">
    <path d="M0 0H545L530 62Q527 75 512 75H33Q18 75 15 62Z" fill="var(--navy)"/>
    <path d="M15 76Q8 80 6 90V236M530 76Q537 80 539 90V236" fill="none" stroke="#cfd0d3" stroke-width="1"/>
  </svg>
  <div class="wordmark"><span class="dot"></span>HALVERN SYSTEMS</div>
  <p class="return"><strong>If undelivered, please return to:</strong>Bellmont House, Level 3, 14 Kestrel Lane, Northbridge, WA 6003</p>
</section>

<section class="piece letterhead" aria-label="Letterhead">
  <div class="wordmark"><span class="dot"></span>HALVERN SYSTEMS</div>
  <div class="masthead-contact">
    <p>Bellmont House<br>Level 3, 14 Kestrel Lane<br>Northbridge, WA 6003</p>
    <p><svg class="icon"><use href="#i-phone"/></svg>+61 8 5550 1234</p>
    <p><svg class="icon"><use href="#i-mail"/></svg>hello@halvernsystems.com.au</p>
    <p><svg class="icon"><use href="#i-web"/></svg>www.halvernsystems.com.au</p>
  </div>
  <div class="letter">
    <p class="greeting">Lorem ipsum dolor,<br>consectetur</p>
    <p>Lorem ipsum dolor sit amet, consectetur adipiscing elit. Duis sed aliquet neque. Fusce mollis placerat leo eu faucibus. Suspendisse suscipit egestas nunc, consequat euismod quam elementum venenatis. Nulla vitae nulla id mauris dictum imperdiet in vitae augue. Suspendisse fringilla bibendum ultrices.</p>
    <p>Sed rhoncus, nisi nec egestas tempus, orci velit ullamcorper dolor, malesuada molestie libero tellus in justo. Duis pharetra, turpis vel ultrices consequat, est ante laoreet nisi, et imperdiet ligula ipsum non quam. In tristique consequat diam, sed semper dolor aliquet et. Cum sociis natoque penatibus et magnis dis parturient montes, nascetur ridiculus mus. Duis sit amet ante mauris, a sodales tellus. Phasellus ante eros, lacinia at eleifend eu, laoreet sed nibh. Nulla rhoncus erat vitae dolor aliquam varius pretium lectus accumsan.</p>
    <p style="margin-top:20px">Aliquam quis lorem eget nibh dignissim accumsan. Proin vitae lectus pretium justo molestie pellentesque. Fusce ultrices risus vitae justo adipiscing id consectetur elit sagittis. Integer nec dapibus tellus. Donec ultricies massa a dolor eleifend ut adipiscing felis feugiat. Praesent fermentum sem felis, vitae vulputate odio. Curabitur faucibus leo quis velit molestie in fringilla ligula mollis. Pellentesque aliquet dolor ut nibh tempor sed vehicula arcu malesuada. Maecenas eget justo at augue molestie ullamcorper non eu est. Cras varius ullamcorper malesuada. Proin ut enim imperdiet augue pulvinar iaculis eget nec ipsum. Fusce sed orci mi. Etiam tristique suscipit ligula non volutpat. Nullam lobortis, enim sed faucibus faucibus, lacus risus euismod ligula, at interdum justo libero a elit. Pellentesque sem ligula, tempor a faucibus auctor, gravida et ante. Donec tristique imperdiet eros et vulputate. Cras id purus id mi volutpat egestas. Cras tellus velit, tristique at dignissim et, tincidunt at felis. Maecenas vestibulum felis eget mauris pellentesque gravida. Nunc commodo tincidunt ornare. Suspendisse quis volutpat lectus. Nunc sed dui sit amet nulla vulputate congue et imperdiet mi.</p>
    <p class="closing">Sincerely</p>
  </div>
</section>

<section class="piece signature" aria-label="Email signature">
  <div class="portrait" role="img" aria-label="Portrait photo of the sender"></div>
  <div class="person">
    <p class="name">Daniel Mercer</p>
    <p class="role">Chief Executive Officer</p>
    <p><svg class="icon"><use href="#i-phone"/></svg>+61 8 5550 1234</p>
    <p><svg class="icon"><use href="#i-mail"/></svg>hello@halvernsystems.com.au</p>
    <p><svg class="icon"><use href="#i-web"/></svg>www.halvernsystems.com.au</p>
  </div>
  <div class="office"><strong>Bellmont House</strong><br>Level 3, 14 Kestrel Lane, Northbridge, WA 6003</div>
  <div class="wordmark"><span class="dot"></span>HALVERN</div>
</section>
</body>
</html>
```